Velmira Banner Ad For Shopping Cart

We need a banner ad for a shopping cart. The ad needs to reflect the fun summer sun feel as it is a summer special.

Here's all the things the ad needs to say:

Beauty Summer Pack Collection Yours when you spend $80 or more.
Keep your skin looking radiant this summer with our Velmira Tulip Dewing Spray, rich in Vitamin C, keeps your pores refined and skin fresh, 100ml worth $29.80. Jojoba Oil keeps skin and hair well hydrated worth $10. Kesh Moisture Lotion in a fresh summer scent (Lavender, Lime and Patchouli) light cream, easily absorbed, great for all skin types, worth $5. Natural Face Brush for cleansing skin, keeping you fresh and clean worth $13.75 and Double-Sided Nail Brush worth $7. All packed in a beautiful cotton drawstring bag.

Limited stock . Only 18 Packs Available.
All skin care is Australian Made and Grown without the use of Pesticides or Chemicals.
To redeem Beauty Pack write in comments box: please include summer pack.

Here's the individual images of what's given away as part of the special please grab them from the site here:
Tulip Dewing Spray - http://shop.velmira-example.com/item-p/tulip-spray.htm
Jojoba Oil - http://shop.velmira-example.com/item-p/argan-drops.htm
Kesh Moisture Lotion - http://shop.velmira-example.com/item-p/kesh-lotion.htm
Natural Face Brush - http://shop.velmira-example.com/item-p/hb-sisal.htm
Double Sided Nail Brush - http://shop.velmira-example.com/item-p/tk07.htm

Below is the website where this design is going to go (currently there is a black placehoder in this space) http://shop.velmira-example.com/

So the design while it needs to stand out and pop off the page it also needs to suit the rest of the page design.

```html
<!DOCTYPE html>
<html lang="en">
<head>
<meta charset="utf-8">
<title>Velmira Beauty Summer Pack</title>
<link rel="stylesheet" href="https://fonts.googleapis.com/css2?family=Arimo:wght@400;700&display=swap">
<style>
  :root {
    --ink-light: #ffffff;
    --ink-soft: #f6e9e9;
    --shade-deep: #1a0406;
    --shade-wine: #4a070c;
    --bottle-red: #e0141c;
    --bottle-glow: #ff4a3c;
    --haze-violet: #6a4a78;
    --haze-warm: #c48a5a;
  }
  * { margin: 0; padding: 0; box-sizing: border-box; }
  html, body {
    width: 1200px;
    height: 594px;
    overflow: hidden;
    background: var(--shade-deep);
  }
  .banner {
    position: relative;
    width: 1200px;
    height: 594px;
    overflow: hidden;
    font-family: "Arimo", Arial, sans-serif;
    color: var(--ink-light);
  }
  .banner__photo {
    position: absolute;
    inset: 0;
    background:
      linear-gradient(90deg, rgba(26,4,6,0) 0%, rgba(26,4,6,0) 58%, rgba(26,4,6,0.55) 72%, rgba(26,4,6,0.35) 100%),
      radial-gradient(ellipse 230px 340px at 400px 330px, var(--bottle-glow) 0%, var(--bottle-red) 45%, rgba(150,10,16,0.85) 80%, rgba(90,6,10,0) 100%),
      radial-gradient(ellipse 140px 120px at 40px 60px, var(--haze-violet) 0%, rgba(106,74,120,0) 100%),
      radial-gradient(ellipse 120px 110px at 30px 520px, var(--haze-warm) 0%, rgba(196,138,90,0) 100%),
      radial-gradient(ellipse 260px 380px at 980px 250px, #7a0c12 0%, rgba(122,12,18,0) 100%),
      linear-gradient(90deg, #2a0c12 0%, var(--shade-wine) 45%, #3a060a 100%);
  }
  .offer {
    position: absolute;
    left: 741px;
    top: 34px;
    width: 445px;
    text-shadow: 0 1px 3px rgba(0,0,0,0.45);
  }
  .offer__headline {
    font-size: 33px;
    font-weight: 700;
    line-height: 40px;
    letter-spacing: -0.2px;
  }
  .offer__details {
    margin-top: 20px;
    font-size: 16.2px;
    line-height: 20px;
    color: var(--ink-soft);
  }
  .offer__stock {
    margin-top: 19px;
    font-size: 16.2px;
    font-weight: 700;
    line-height: 20px;
  }
  .offer__origin {
    margin-top: 21px;
    font-size: 16.2px;
    line-height: 20px;
    color: var(--ink-soft);
  }
  .offer__redeem {
    margin-top: 20px;
    font-size: 16.2px;
    font-weight: 700;
    line-height: 21px;
  }
</style>
</head>
<body>
  <div class="banner">
    <div class="banner__photo" role="img" aria-label="Close-up photograph of a glass bottle filled with red rose mist against a dark blurred background"></div>
    <section class="offer">
      <h1 class="offer__headline">Beauty Summer Pack Collection Yours when you spend $80 or more.</h1>
      <p class="offer__details">Keep your skin looking radiant this summer with our Velmira Tulip Dewing Spray, rich in Vitamin C, keeps your pores refined and skin fresh, 100ml worth $29.80. Jojoba Oil keeps skin and hair well hydrated worth $10. Kesh Moisture Lotion in a fresh summer scent (Lavender, Lime and Patchouli) light cream, easily absorbed, great for all skin types, worth $5. Natural Face Brush for cleansing skin, keeping you fresh and clean worth $13.75 and Double-Sided Nail Brush worth $7. All packed in a beautiful cotton drawstring bag.</p>
      <p class="offer__stock">Limited stock . Only 18 Packs Available.</p>
      <p class="offer__origin">All skin care is Australian Made and Grown without the use of Pesticides or Chemicals.</p>
      <p class="offer__redeem">To redeem Beauty Pack write in comments box: please include summer pack.</p>
    </section>
  </div>
</body>
</html>
```